Tandra Link and recovery web and app design

GPS enabled APP providing breakdown and assistance for cyclists by cyclists.
24 hour bicycle assist and recovery package for both road and off road cyclists.
First and only bicycle assist package whose aim is to get you back on your bike to complete your journey

I need the design package to give a website designer so they can build website and app. I have a logo done by my nephew which is the company logo but i need a full design package now.

Below is the website banner I have now and the logo
Updates

Reason: I am moving house today and have no internet till Tuesday so please extend deadline 5 days to allow everyone

Target Market(s)

Cyclists in the South East and London, and then all UK, includes MTB off road and road cyclists. Please see farrowspinline.co.uk as this was my pretotype website for market information.

Number of Pages Required

5+ page

Font styles to use
Other font styles liked:
• FARROW SPINLINE

Colors
ffcf3e
f04b51
f68d4c
faa54b
fbee3f
add136

Requirements
Must have
• Landing page, mechanical page, medical page, FAQ page, policy information page accessible by policy holder to update, lost password page, quote page, pay page, contact us page, all policy info must be accessible by Norvane Desk out operations room provider,
Nice to have
• Lots of great action cycling photos and very usable website

```html
<!DOCTYPE html>
<html lang="en">
<head>
<meta charset="utf-8">
<title>Farrow Spinline – Tandra Link</title>
<link rel="stylesheet" href="https://fonts.googleapis.com/css2?family=Lato:wght@400;700;900&display=swap">
<style>
:root{
  --red:#ef4b51;
  --red-soft:#f16a6f;
  --ink:#2b2b2b;
  --text:#444;
  --white:#fff;
  --frame:#e6e6e6;
  --field:#7a7a7a;
  --dark:#1c1c1c;
  --social:#3b5a9a;
}
*{box-sizing:border-box;margin:0;padding:0}
html,body{width:1200px;height:2594px;overflow:hidden}
body{background:var(--frame);font-family:"Lato",Arial,sans-serif;color:var(--text)}
.page{position:absolute;left:14px;top:14px;width:1172px;height:2566px;background:var(--white);overflow:hidden}

/* header */
.site-header{height:141px;position:relative}
.brand{position:absolute;left:36px;top:40px;display:flex;align-items:center;gap:20px}
.brand-dot{width:56px;height:56px;border-radius:50%;background:var(--red)}
.brand-name{font-weight:900;font-size:26px;color:var(--red)}
.header-actions{position:absolute;right:34px;top:56px;display:flex;align-items:center;gap:38px}
.social-dot{width:18px;height:18px;border-radius:50%;background:var(--social)}
.btn{display:inline-block;background:var(--red);color:var(--white);font-weight:700;text-transform:uppercase;border-radius:3px;text-align:center}
.btn-header{font-size:14px;padding:8px 18px}

.main-nav{height:35px;background:var(--red);display:flex;justify-content:space-around;align-items:center;padding:0 60px 0 40px}
.main-nav a{color:var(--white);font-weight:700;font-size:15px;text-decoration:none}

/* hero */
.hero{position:relative;height:490px}
.hero-photo{position:absolute;inset:0;background:linear-gradient(100deg,#c9d7e6 0%,#7d8a97 22%,#4b6aa6 40%,#889c5a 58%,#a58a4c 78%,#6c7a3e 100%)}
.message-panel{position:absolute;left:781px;top:70px;width:323px;height:354px;background:rgba(20,20,20,.82);border:2px solid #d7d7d7;border-radius:4px}
.message-title{position:absolute;left:-12px;top:24px;width:334px;height:38px;background:var(--red);color:var(--white);font-weight:700;font-size:18px;text-align:center;line-height:38px}
.message-fields{position:absolute;left:26px;top:84px;width:279px}
.message-fields .field{height:30px;background:rgba(196,58,64,.85);color:var(--white);font-size:13px;padding:6px 14px;margin-bottom:10px}
.message-fields .field.tall{height:90px}
.message-send{position:absolute;left:66px;top:308px;width:200px;height:30px;background:linear-gradient(#d84a50,#9b2a30);color:var(--white);font-weight:700;font-size:14px;text-align:center;line-height:30px}
.slider-strip{height:32px;background:var(--red-soft);display:flex;justify-content:center;align-items:center;gap:6px}
.slider-strip span{width:11px;height:11px;border-radius:50%;background:var(--white)}
.slider-strip span.active{background:#b21f25}

/* features */
.features{height:291px;background:var(--red);display:flex;justify-content:space-around;padding:40px 80px 0 70px}
.feature{width:240px;text-align:center;color:var(--white);font-size:16px;line-height:22px}
.feature-icon{width:110px;height:110px;border:3px solid var(--white);border-radius:6px;margin:0 auto 20px;display:flex;align-items:center;justify-content:center}

/* promo */
.promo{position:relative;height:290px}
.promo-photo{position:absolute;inset:0;background:linear-gradient(90deg,#3a2c2c,#5a4a48 30%,#2c2f3a 60%,#4d3a38)}
.promo-photo::after{content:"";position:absolute;inset:0;background:rgba(0,0,0,.55)}
.promo-box{position:absolute;left:380px;top:30px;width:412px;height:232px;background:rgba(0,0,0,.75);border:2px solid #ddd;border-radius:5px;text-align:center;color:var(--white)}
.promo-title{margin-top:22px;color:var(--red);font-weight:900;font-size:25px;line-height:26px;position:relative}
.promo-title small{display:block;font-size:19px}
.promo-title::before,.promo-title::after{content:"";position:absolute;top:14px;width:40px;height:2px;background:var(--red)}
.promo-title::before{left:20px}.promo-title::after{right:20px}
.promo-price{margin:14px 38px 0;border-top:2px solid var(--white);border-bottom:2px solid var(--white);padding:14px 0;font-size:22px;font-weight:700}
.btn-promo{margin-top:24px;font-size:14px;padding:6px 14px;border-radius:4px}

/* service photos */
.service-photos{display:flex;height:330px;position:relative}
.service-photos .photo{flex:1}
.photo-mtb{background:linear-gradient(160deg,#9fc0e0,#b8a58a 45%,#6f7a45 80%)}
.photo-road{background:linear-gradient(200deg,#c9b49a,#8a7360 40%,#5a4c44 80%)}
.service-photos svg{position:absolute;left:0;bottom:-1px}

/* services */
.services{display:flex;height:337px;padding:30px 0 0 36px}
.service{width:586px;position:relative;padding-left:90px}
.service-icon{position:absolute;left:0;top:0}
.service h2{color:var(--red);font-weight:900;font-size:31px;line-height:34px}
.service h3{color:var(--ink);font-weight:900;font-size:17.5px;line-height:21px;margin-top:6px;text-transform:uppercase;width:390px}
.service p{font-size:16px;line-height:22px;margin-top:18px;width:425px}
.btn-service{margin:20px 0 0 54px;width:300px;font-size:16px;padding:10px 0;box-shadow:0 3px 4px rgba(0,0,0,.2)}
.service.medical{padding-left:100px}
.service.medical .service-icon{left:-2px}

.quote-band{height:81px;background:var(--red);color:var(--white);font-weight:900;font-size:31px;text-align:center;line-height:81px}

/* contact */
.contact{position:relative;height:260px}
.contact-photo{position:absolute;inset:0;background:linear-gradient(90deg,#b9b3ab,#d9d2c6 40%,#c7cfd6 70%,#aab6c0)}
.contact-photo::after{content:"";position:absolute;inset:0;background:rgba(255,255,255,.6)}
.contact h2{position:absolute;top:30px;width:100%;text-align:center;color:var(--ink);font-weight:900;font-size:25px}
.contact-form{position:absolute;left:282px;top:84px;width:610px;display:grid;grid-template-columns:300px 300px;gap:10px}
.contact-form .field{height:38px;background:var(--field);color:var(--white);font-size:14px;padding:10px 14px}
.contact-form .message{grid-column:2;grid-row:1/3;height:86px}
.contact-form .send{width:104px;height:38px;background:var(--dark);color:var(--white);font-weight:700;text-align:center;line-height:38px;font-size:14px}

/* footer */
.site-footer{position:relative;height:271px}
.footer-col{position:absolute;top:36px}
.footer-col h4{color:var(--red);font-weight:900;font-size:15px;margin-bottom:16px}
.quick-links{left:62px}
.quick-links li{list-style:none;font-weight:700;font-size:13px;color:var(--ink);line-height:21px;text-transform:uppercase}
.newsletter{left:306px;width:240px}
.newsletter p{font-weight:700;font-size:13px;color:var(--ink);line-height:18px}
.newsletter .email{margin-top:16px;width:230px;height:36px;background:#cfcfcf;color:#666;font-size:13px;padding:10px 14px}
.newsletter .subscribe{margin-top:16px;width:104px;height:36px;background:var(--dark);color:var(--white);font-weight:700;font-size:13px;text-align:center;line-height:36px}
.contact-info{left:630px;width:260px}
.contact-info li{list-style:none;display:flex;gap:14px;font-weight:700;font-size:13px;color:var(--ink);line-height:18px;margin-bottom:18px}
.contact-info svg{flex:none;margin-top:1px}
.contact-info .social-dot{width:14px;height:14px;background:var(--ink);margin-left:12px}
.footer-brand{position:absolute;left:916px;top:70px;text-align:center}
.footer-brand .brand-dot{margin:0 auto 14px;width:50px;height:50px}
.footer-brand span{font-weight:900;font-size:21px;color:var(--red)}
.copyright{position:absolute;bottom:10px;width:100%;text-align:center;font-size:11px;color:var(--ink)}
</style>
</head>
<body>
<div class="page">

  <header class="site-header">
    <div class="brand"><span class="brand-dot"></span><span class="brand-name">FARROW SPINLINE</span></div>
    <div class="header-actions"><span class="social-dot"></span><span class="btn btn-header">Bike Recovery Quote</span></div>
  </header>

  <nav class="main-nav">
    <a>MECHANICAL</a><a>MEDICAL</a><a>FAQ</a><a>BIKE RECOVERY QUOTE</a><a>PAYMENT</a><a>CONTACT</a>
  </nav>

  <section class="hero">
    <div class="hero-photo" role="img" aria-label="Road cyclist riding at speed through a hilly landscape under a blue sky"></div>
    <div class="message-panel">
      <div class="message-title">SEND US A MESSAGE</div>
      <div class="message-fields">
        <div class="field">Name</div>
        <div class="field">Email Address</div>
        <div class="field">Phone Number</div>
        <div class="field tall">Message</div>
      </div>
      <div class="message-send">SEND MESSAGE</div>
    </div>
  </section>
  <div class="slider-strip"><span class="active"></span><span></span><span></span><span></span></div>

  <section class="features">
    <div class="feature">
      <div class="feature-icon">
        <svg width="80" height="80" viewBox="0 0 80 80"><circle cx="40" cy="40" r="34" fill="none" stroke="#fff" stroke-width="4"/><g fill="#fff"><circle cx="28" cy="28" r="4"/><circle cx="40" cy="28" r="4"/><circle cx="52" cy="28" r="4"/><circle cx="28" cy="40" r="4"/><circle cx="40" cy="40" r="4"/><circle cx="52" cy="40" r="4"/><circle cx="28" cy="52" r="4"/><circle cx="40" cy="52" r="4"/><circle cx="52" cy="52" r="4"/></g></svg>
      </div>
      GPS enabled APP providing breakdown and assistance for cyclists by cyclists.
    </div>
    <div class="feature">
      <div class="feature-icon">
        <svg width="80" height="80" viewBox="0 0 80 80"><path d="M64 40a24 24 0 1 1-8-18" fill="none" stroke="#fff" stroke-width="5"/><path d="M52 12l10 10-13 3z" fill="#fff"/><text x="40" y="49" text-anchor="middle" font-family="Lato,sans-serif" font-weight="900" font-size="24" fill="#fff">24</text></svg>
      </div>
      24 hour Tandra Link and recovery package for both road and off road cyclists.
    </div>
    <div class="feature">
      <div class="feature-icon">
        <svg width="80" height="80" viewBox="0 0 80 80"><circle cx="22" cy="52" r="14" fill="#fff"/><circle cx="58" cy="52" r="14" fill="#fff"/><path d="M22 52l16-20 20 20M38 32h12" fill="none" stroke="#fff" stroke-width="4"/></svg>
      </div>
      First and only Tandra Link package whose aim is to get you back on your bike to complete your journey.
    </div>
  </section>

  <section class="promo">
    <div class="promo-photo" role="img" aria-label="Group of road racers riding in a pack"></div>
    <div class="promo-box">
      <div class="promo-title">START YOUR OWN<small>TANDRA LINK PACKAGE</small></div>
      <div class="promo-price">FROM ONLY £4.99/MONTH</div>
      <span class="btn btn-promo">BIKE RECOVERY QUOTE &nbsp;➜</span>
    </div>
  </section>

  <section class="service-photos">
    <div class="photo photo-mtb" role="img" aria-label="Mountain biker riding down a rocky trail"></div>
    <div class="photo photo-road" role="img" aria-label="Cyclocross riders racing side by side"></div>
    <svg width="1172" height="40" viewBox="0 0 1172 40" preserveAspectRatio="none"><path d="M0 0L586 40L1172 0V40H0z" fill="#fff"/></svg>
  </section>

  <section class="services">
    <article class="service mechanical">
      <svg class="service-icon" width="72" height="64" viewBox="0 0 72 64"><circle cx="26" cy="26" r="16" fill="none" stroke="#ef4b51" stroke-width="6" stroke-dasharray="6 4"/><circle cx="26" cy="26" r="6" fill="none" stroke="#ef4b51" stroke-width="4"/><path d="M40 40l22 20" stroke="#ef4b51" stroke-width="7" stroke-linecap="round"/></svg>
      <h2>MECHANICAL</h2>
      <h3>Off road MTB cover and roadside mechanical cover</h3>
      <p>At Farrow Spinline we want you and your bike to be in perfect working order so join us now and we will annually service your bike at our expense via our network of trained cycle mechanic and local bike shops.</p>
      <span class="btn btn-service">LEARN MORE ON MECHANICAL</span>
    </article>
    <article class="service medical">
      <svg class="service-icon" width="72" height="72" viewBox="0 0 72 72"><path d="M28 8h16v20h20v16H44v20H28V44H8V28h20z" fill="#ef4b51"/></svg>
      <h2>MEDICAL</h2>
      <h3>Off road MTB cover and roadside medical cover</h3>
      <p>Join our premium assistance package and an enhanced first aid kit specifically designed for cycling injuries will be delivered to your location by our mechanics for your personal use.</p>
      <span class="btn btn-service">LEARN MORE ON MEDICAL</span>
    </article>
  </section>

  <div class="quote-band">GET A RECOVERY QUOTE NOW</div>

  <section class="contact">
    <div class="contact-photo" role="img" aria-label="Faded city riverside skyline with a bridge"></div>
    <h2>CONTACT US</h2>
    <div class="contact-form">
      <div class="field">Name</div>
      <div class="field message">Message</div>
      <div class="field">Email</div>
      <div class="field">Phone</div>
      <div class="send">SEND</div>
    </div>
  </section>

  <footer class="site-footer">
    <div class="footer-col quick-links">
      <h4>QUICK LINKS</h4>
      <ul><li>Mechanical</li><li>Medical</li><li>FAQ</li><li>Bike Recovery Quote</li><li>Payment</li><li>Contact</li></ul>
    </div>
    <div class="footer-col newsletter">
      <h4>NEWSLETTER SIGN UP</h4>
      <p>Stay informed about company news by signing up for our Newsletters.</p>
      <div class="email">Email</div>
      <div class="subscribe">SUBSCRIBE</div>
    </div>
    <div class="footer-col contact-info">
      <h4>CONTACT INFO</h4>
      <ul>
        <li><svg width="12" height="16" viewBox="0 0 12 16"><path d="M6 0a6 6 0 0 1 6 6c0 4-6 10-6 10S0 10 0 6a6 6 0 0 1 6-6z" fill="#2b2b2b"/><circle cx="6" cy="6" r="2" fill="#fff"/></svg><span>48 Kestrel Row<br>London</span></li>
        <li><svg width="16" height="14" viewBox="0 0 16 14"><path d="M1 4c0-3 14-3 14 0v2h-4V4H5v2H1z M3 7h10l2 7H1z" fill="#2b2b2b"/></svg><span>+44 20 7946 0321</span></li>
        <li><svg width="16" height="12" viewBox="0 0 16 12"><rect width="16" height="12" fill="#2b2b2b"/><path d="M0 0l8 7 8-7" fill="none" stroke="#fff" stroke-width="1.5"/></svg><span>info@farrowspinline.co.uk</span></li>
        <li><span class="social-dot"></span></li>
      </ul>
    </div>
    <div class="footer-brand"><div class="brand-dot"></div><span>FARROW SPINLINE</span></div>
    <div class="copyright">© 2015 FARROW SPINLINE. ALL RIGHTS RESERVED.</div>
  </footer>

</div>
</body>
</html>
```